Flyer for American Indian Elders on Dementia Warning Signs

We need a flyer designed for older adults who are American Indian or Alaska Native (in the U.S.).

Ideally, the flyer should complement the colors of our logos. The project logo and our organization logo are attached to the brief.

When people see the flyer we want them to feel that it represents their culture, is warm, and professional but relatable to older adults and people who have limited incomes.

I have attached an earlier draft of the document we designed ourselves BUT we want different and better.

It is for older adults who have trouble reading so:
1. you must use a font that is 11.5 points or larger
2. Do not put text over complex pictures or use shading with words
3. You can use a serif font for the heading, but should use san serif for the body text
4. There should be good contrast between the font color and background

Please do not use any images that include a head dress or pictures of American Indian people or things that are very traditional or "token" imagery.

We need to save a small space under the call out box/ somewhere on the flyer for other people to add their logo once they download.

Let us know if you have questions or need additional information.

Target Market(s)

Older American Indian people

Font styles to use
Serif
Sans Serif

Requirements
Must have
• Easy to read for older adults
Should not have
• indian headdress

```html
<!DOCTYPE html>
<html lang="en">
<head>
<meta charset="UTF-8">
<title>10 Warning Signs of Abnormal Memory Changes or Dementia</title>
<link href="https://fonts.googleapis.com/css2?family=Montserrat:wght@400;600;700;800&family=Oswald:wght@500;600&family=PT+Sans+Narrow&family=Tinos:wght@700&display=swap" rel="stylesheet">
<style>
  :root{
    --canvas:#c4c5c7;
    --paper:#ffffff;
    --teal:#6db5bf;
    --teal-dark:#5aa8b4;
    --rust:#b24f47;
    --ink:#1d1d1d;
    --rose:#97736f;
    --num-bg:#ebebeb;
  }
  *{box-sizing:border-box;margin:0;padding:0}
  html,body{width:1200px;height:1200px;overflow:hidden;background:var(--canvas)}
  .flyer{position:absolute;left:137px;top:0;width:926px;height:1200px;background:var(--paper);overflow:hidden;font-family:"PT Sans Narrow",sans-serif;color:var(--ink)}

  .big-ten{position:absolute;left:45px;top:50px;width:135px;height:136px;background:var(--teal);color:#fff;font-family:"Tinos",serif;font-weight:700;font-size:128px;line-height:136px;text-align:center;letter-spacing:-8px}
  .title{position:absolute;left:195px;top:50px;font-family:"Montserrat",sans-serif;font-weight:700;font-size:31px;line-height:32.5px;text-transform:uppercase}
  .title .teal{color:var(--teal-dark)}
  .title .rust{color:var(--rust)}

  .timeline{position:absolute;left:106px;top:186px;width:2px;height:950px;background:var(--teal)}
  .timeline-dot{position:absolute;left:101px;top:1131px;width:12px;height:12px;border-radius:50%;background:var(--teal)}
  .timeline-notch{position:absolute;left:101px;top:182px;width:0;height:0;border-left:6px solid transparent;border-right:6px solid transparent;border-top:6px solid var(--teal)}
  .num{position:absolute;left:79px;width:56px;height:56px;background:var(--num-bg);color:var(--teal);font-family:"Montserrat",sans-serif;font-weight:600;font-size:44px;line-height:56px;text-align:center}

  .sign{position:absolute;left:156px;width:345px}
  .sign .icon{position:absolute;left:0;top:-4px;width:38px;height:38px}
  .sign h2{padding-left:46px;font-family:"Oswald",sans-serif;font-weight:500;font-size:16px;line-height:22px;color:var(--rust);text-transform:uppercase;letter-spacing:.1px}
  .sign p{margin-top:7px;font-size:15px;line-height:21px}
  .sign p.wide{width:372px;margin-top:2px;font-family:"Montserrat",sans-serif;font-size:13.5px;line-height:21px;padding-left:6px}
  .sign p.tiny{font-size:11.5px;line-height:12px;margin-top:6px}

  .hero{position:absolute;left:490px;top:0;width:436px;height:490px}

  .partner{position:absolute;left:576px;top:489px;display:flex;align-items:center;gap:12px}
  .partner-mark{width:68px;height:68px;border-radius:50%;border:3px solid var(--teal)}
  .partner-name{font-family:"Montserrat",sans-serif;font-weight:600;font-size:17px;line-height:20px;color:var(--teal-dark);text-transform:uppercase}

  .callout{position:absolute;left:569px;top:639px;width:305px;height:411px;background:var(--teal);color:#fff;font-size:17px;line-height:22.5px;text-align:center;padding:44px 22px 0}
  .callout p{margin-bottom:23px}
  .callout p:first-child{margin-bottom:42px}
  .learn{position:absolute;left:569px;top:1050px;width:305px;height:150px;background:var(--rose);color:#fff;font-size:17px;line-height:22.5px;text-align:center;padding:10px 12px 0}
  .learn .url{display:block;font-size:18px;line-height:25px}
</style>
</head>
<body>
<div class="flyer">

  <div class="big-ten">10</div>
  <h1 class="title">
    <span class="teal">Warning Sings</span><br>
    of Abnormal<br>
    <span class="rust">Memory Changes</span><br>
    or Dementia
  </h1>

  <div class="timeline-notch"></div>
  <div class="timeline"></div>
  <div class="timeline-dot"></div>

  <div class="num" style="top:223px">1</div>
  <div class="num" style="top:324px">2</div>
  <div class="num" style="top:405px">3</div>
  <div class="num" style="top:476px">4</div>
  <div class="num" style="top:566px">5</div>
  <div class="num" style="top:654px">6</div>
  <div class="num" style="top:759px">7</div>
  <div class="num" style="top:851px">8</div>
  <div class="num" style="top:944px">9</div>
  <div class="num" style="top:1049px;font-size:40px;letter-spacing:-2px">10</div>

  <section class="sign" style="top:236px">
    <svg class="icon" viewBox="0 0 38 38" fill="none" stroke="#b24f47" stroke-width="1.6"><circle cx="17" cy="21" r="14"/><path d="M17 11v20M11 16h12M11 25h12"/><circle cx="31" cy="7" r="5"/><path d="M31 4v5l-2-2M31 9l2-2"/></svg>
    <h2>Memory loss that affectsyour daily life</h2>
    <p>You may Forget events or important dates Repeat yourself&nbsp; Rely more often on lists or sticky notes to remember things</p>
  </section>

  <section class="sign" style="top:327px">
    <svg class="icon" viewBox="0 0 38 38" fill="none" stroke="#b24f47" stroke-width="1.6"><path d="M16 8a13 13 0 1 0 13 13H16z"/><path d="M20 4a13 13 0 0 1 13 13H20z"/><circle cx="34" cy="3" r="2"/><circle cx="35" cy="31" r="2"/></svg>
    <h2>Trouble planning or&nbsp; solving problems</h2>
    <p>You may have a harder time: Paying bills Cooking recipes you have used&nbsp; for years</p>
  </section>

  <section class="sign" style="top:410px">
    <svg class="icon" viewBox="0 0 38 38" fill="none" stroke="#b24f47" stroke-width="1.8"><circle cx="19" cy="19" r="15"/><path d="M19 10v10l7 4"/></svg>
    <h2>Get confused about the time, date, or<br>where you are.</h2>
  </section>

  <section class="sign" style="top:472px">
    <svg class="icon" viewBox="0 0 38 38" fill="none" stroke="#b24f47" stroke-width="1.8"><rect x="4" y="5" width="22" height="28" rx="2"/><path d="M11 3h8v5h-8zM9 19l4 4 8-9"/><path d="M30 20l4 4-6 8-4 1 1-4z"/></svg>
    <h2>Daily tasks are&nbsp; getting harder</h2>
    <p>including Driving Making a grocery list&nbsp; or going shopping</p>
  </section>

  <section class="sign" style="top:534px">
    <svg class="icon" viewBox="0 0 38 38" fill="none" stroke="#b24f47" stroke-width="1.6"><path d="M14 36v-6l-6-2 2-6-4-3 3-6c2-6 9-9 15-7"/><circle cx="27" cy="13" r="5"/><path d="M27 4v3M27 19v3M18 13h3M33 13h3"/></svg>
    <h2>Troublewith how your eyesight and thinking work together&nbsp; that<br>&nbsp;gets worse</h2>
    <p class="wide">This includesTripping, falls, or problems with your balance Spilling or dropping things more</p>
  </section>

  <section class="sign" style="top:661px">
    <svg class="icon" viewBox="0 0 38 38" fill="none" stroke="#b24f47" stroke-width="1.6"><path d="M4 8h18M4 13h22M4 18h16M4 23h20M4 28h14"/><path d="M30 10l4 2-8 18-4-2z"/><path d="M6 30v6l4-4"/></svg>
    <h2>New troubletalking or writing</h2>
    <p>You have a hard time finding the words you want to say. For example, you may say “that thing on your wrist that tells time” instead of “watch.”</p>
  </section>

  <section class="sign" style="top:765px">
    <svg class="icon" viewBox="0 0 38 38" fill="none" stroke="#b24f47" stroke-width="1.5"><circle cx="12" cy="10" r="5"/><path d="M10 15v4h4v-4M12 1v2M3 10h2M19 10h2M5 3l2 2M19 3l-2 2"/><circle cx="29" cy="28" r="4"/><path d="M29 21v3M29 32v3M22 28h3M33 28h3"/></svg>
    <h2>Loseand cannot find things</h2>
    <p>For example, you Can’t find the coffee pot that you use every day Mightput your car keys in the freezer</p>
  </section>

  <section class="sign" style="top:845px">
    <svg class="icon" viewBox="0 0 38 38" fill="none" stroke="#b24f47" stroke-width="1.5"><circle cx="19" cy="15" r="7"/><path d="M8 36c0-7 5-12 11-12s11 5 11 12M19 26v6"/><path d="M19 2v3M8 5l2 2M30 5l-2 2M4 14h3M31 14h3"/></svg>
    <h2 style="line-height:25px">Notice changes&nbsp; in your<br>mood or personality</h2>
    <p style="margin-top:2px">such as being Easily mad or sad in everyday&nbsp; situtions<br>&nbsp;More fearful&nbsp; (scared) or suspicious (not trusting)</p>
  </section>

  <section class="sign" style="top:942px;left:152px">
    <svg class="icon" viewBox="0 0 38 38" fill="none" stroke="#b24f47" stroke-width="1.5"><circle cx="19" cy="8" r="5"/><path d="M10 26l3-11h12l3 11M2 30h34M8 30l3 6h16l3-6"/></svg>
    <h2 style="line-height:25px">Make poorchoices.this&nbsp; may<br>make you more likely to</h2>
    <p style="margin-top:0">Spend money you do not have or be a scam victim Stop washing up regularly or pay less attention to how you look Forget to take care of your pet</p>
  </section>

  <section class="sign" style="top:1059px">
    <svg class="icon" viewBox="0 0 38 38" fill="none" stroke="#b24f47" stroke-width="1.5"><circle cx="12" cy="8" r="4"/><circle cx="26" cy="8" r="4"/><path d="M19 24l-5-5a3 3 0 0 1 5-3 3 3 0 0 1 5 3z"/><path d="M2 20l6 10h10M36 20l-6 10H20"/></svg>
    <h2 style="line-height:20px">Pull away from friends and family<br>because&nbsp; it is harder to keep up</h2>
    <p class="tiny">You may not want to do things you used to enjoy, like sporting events, church, music, or sex.</p>
  </section>

  <svg class="hero" viewBox="0 0 436 490" role="img" aria-label="Illustration of a glowing human brain inside a head held by a hand">
    <defs>
      <linearGradient id="swoosh" x1="0" y1="0" x2="0" y2="1">
        <stop offset="0" stop-color="#6aaeb6"/>
        <stop offset="1" stop-color="#9a6f6c"/>
      </linearGradient>
      <radialGradient id="brain" cx="0.5" cy="0.3" r="0.75">
        <stop offset="0" stop-color="#e0305a"/>
        <stop offset="0.28" stop-color="#5a3fd0"/>
        <stop offset="0.6" stop-color="#1650c8"/>
        <stop offset="1" stop-color="#061a5a"/>
      </radialGradient>
    </defs>
    <path d="M436 40C380 -5 250 0 165 80 90 150 30 250 72 300 40 240 70 160 130 110 80 190 100 360 200 430 260 475 380 470 436 420Z" fill="url(#swoosh)"/>
    <circle cx="240" cy="237" r="195" fill="url(#brain)"/>
  </svg>

  <div class="partner">
    <div class="partner-mark"></div>
    <div class="partner-name">Cedar Ridge Center<br>for Brain Health</div>
  </div>

  <div class="callout">
    <p>American Indian and Alaska Native people have a higher risk of dementia. than White people.</p>
    <p>Big changes in memory or thinking that make it hard to get through the day are not a normal part of aging.</p>
    <p>People with one or more of these 10 signs should talk to their doctor to find the cause. It is not always dementia.</p>
    <p>Early dementia diagnosis gives you a chance to get care and plan your future.</p>
  </div>

  <div class="learn">
    To learn more about the warning signs of de-mentia in American Indian and Alaska Native people, visit:
    <span class="url">www.CedarRidgeBrain.org</span>
    <span class="url">www.healthyagingnow.org</span>
  </div>

</div>
</body>
</html>
```